Website Design for a New Business Sharing Application

Purpose: Website for a new product – a sharing application called "Pondly.io"

Product concept: Easy sharing of business information. The application has different sections: tasks, calendars, documents, contacts, notes and links. The key feature of the application is that you can drag and drop information from different sections into a "share." A share is a page which lists all the types of information that you drag into it. You can add people to this "share."

Note: The application itself is not part of this project, just the website.

Website details: The site, in addition to being informational, will actually be the first point of entry for visitors into the application itself. Because of that, we would like the website design to reflect the look of the application, to create a smooth and seamless experience for the user moving from the website into the application (tough the website does not need to look *exactly* like the application). Included Product Tour screenshots show you the look of the application.

Website pages to be created: 4 pages
We are flexible in terms of the exact structure and placement of elements. You may change that any way you like. The pages are as follows:

Home page
Product Tour page
Press page
Blog page

Specific description of pages are provided in project files we will upload. We will also upload the logo, home page layout we have in mind, and other supporting files.

NOTE: Please submit first the design of the home page. Based on this design we will ask selected designers to submit designs for the other pages.

Target Market(s)

Business people who want to share work related files with their colleagues

Industry/Entity Type

Business

Requirements
Must have
• All the required features are listed in the description of the website and specific pages that we will upload.

```html
<!DOCTYPE html>
<html lang="en">
<head>
<meta charset="utf-8">
<title>Pondly.io — Share NOW</title>
<link href="https://fonts.googleapis.com/css2?family=Open+Sans:wght@400;500;600;700&family=Nunito:wght@800;900&family=Nothing+You+Could+Do&display=swap" rel="stylesheet">
<style>
  :root {
    --page-bg: #ffffff;
    --panel-bg: #f1f1f1;
    --panel-border: #e2e2e2;
    --brand-blue: #2f7db8;
    --headline-blue: #3f88c2;
    --button-blue-dark: #3a78b0;
    --text-grey: #555555;
    --text-dark: #3a3a3a;
    --accent-orange: #d4521c;
    --accent-orange-light: #e8702f;
    --field-border: #cfcfcf;
    --arrow-fill: #e2e2e2;
    --white: #ffffff;
    --strike-red: #c0392b;
  }
  * { box-sizing: border-box; margin: 0; padding: 0; }
  html, body {
    width: 1200px; height: 675px; overflow: hidden;
    background: var(--page-bg);
    font-family: "Open Sans", Arial, sans-serif;
  }
  .canvas { position: relative; width: 1200px; height: 675px; overflow: hidden; }

  .brand { position: absolute; left: 112px; top: 26px; display: flex; align-items: center; gap: 8px; }
  .brand-dot { width: 30px; height: 30px; border-radius: 50%; background: var(--accent-orange); }
  .brand-name { font-size: 28px; font-weight: 700; color: var(--brand-blue); letter-spacing: -0.3px; }

  .access-link {
    position: absolute; right: 122px; top: 38px;
    font-size: 20px; color: #6b6b6b; text-decoration: underline;
  }

  .hero-panel {
    position: absolute; left: 64px; top: 84px; width: 1068px; height: 500px;
    background: var(--panel-bg); border: 2px solid var(--panel-border); border-radius: 9px;
  }

  .script {
    position: absolute; font-family: "Nothing You Could Do", cursive;
    color: var(--brand-blue); line-height: 1.2; transform-origin: center center; white-space: nowrap;
  }
  .script-fast { left: 88px; top: 150px; width: 230px; font-size: 20px; text-align: center; transform: rotate(-27deg); }
  .script-social { left: 928px; top: 136px; width: 110px; font-size: 19px; text-align: center; transform: rotate(30deg); }

  .arrow-area { position: absolute; background: var(--arrow-fill); border-radius: 20px; }
  .arrow-left { left: 204px; top: 192px; width: 216px; height: 40px; }
  .arrow-right { left: 800px; top: 164px; width: 152px; height: 58px; }

  .headline {
    position: absolute; left: 0; width: 1200px; top: 140px; text-align: center;
    font-family: "Nunito", Arial, sans-serif; font-weight: 900; font-size: 60px; letter-spacing: 0.5px;
    color: var(--headline-blue);
    text-shadow: 2px 2px 0 var(--white), -2px -2px 0 var(--white), 2px -2px 0 var(--white), -2px 2px 0 var(--white), 3px 5px 7px rgba(0,0,0,0.35);
  }

  .tagline { position: absolute; left: 404px; top: 262px; font-size: 21px; color: var(--text-grey); }
  .boom {
    position: absolute; left: 722px; top: 228px; width: 124px; height: 104px;
    background: var(--accent-orange); border-radius: 50%;
    display: flex; align-items: center; justify-content: center;
    color: var(--white); font-size: 14px; font-weight: 700;
  }

  .categories {
    position: absolute; left: 0; width: 1200px; top: 348px; text-align: center;
    font-size: 16.5px; font-weight: 500; color: var(--text-dark);
  }
  .categories .sep { margin: 0 13px; }

  .drop-zone {
    position: absolute; left: 108px; top: 401px; width: 450px; height: 80px;
    background: var(--white); border: 2px solid #dcdcdc; border-radius: 7px;
    box-shadow: 0 1px 3px rgba(0,0,0,0.12);
  }
  .drop-plus { position: absolute; left: 68px; top: 14px; width: 48px; height: 48px; }
  .drop-text {
    position: absolute; left: 140px; top: 14px; width: 260px; text-align: center;
    font-size: 20px; color: #2d6ea5; line-height: 26px; letter-spacing: 0.3px;
  }

  .or-word { position: absolute; left: 582px; top: 422px; font-size: 26px; color: #6a6a6a; text-decoration: underline; }

  .email-field {
    position: absolute; left: 638px; top: 401px; width: 451px; height: 44px;
    background: var(--white); border: 2px solid var(--field-border); border-radius: 5px;
    padding: 8px 12px; font-size: 19px; color: #666; letter-spacing: 0.3px;
  }
  .start-button {
    position: absolute; left: 638px; top: 455px; width: 451px; height: 45px;
    border-radius: 5px; border: 2px solid #f1d7c9;
    background: linear-gradient(to bottom, var(--accent-orange-light), var(--accent-orange) 55%, #c24812);
    color: var(--white); font-size: 20.5px; font-weight: 700; text-align: center; line-height: 41px; letter-spacing: 0.5px;
  }

  .info-button {
    position: absolute; top: 518px; width: 228px; height: 45px;
    border: 2px solid #dfe7ef; border-radius: 4px;
    background: linear-gradient(to bottom, #5597cf, var(--button-blue-dark));
    color: var(--white); font-size: 20px; font-weight: 700; letter-spacing: 0.4px;
    display: flex; align-items: center; justify-content: center; gap: 12px;
    box-shadow: 0 2px 3px rgba(0,0,0,0.25);
  }
  .info-button svg { width: 26px; height: 26px; }
  .button-what { left: 330px; }
  .button-video { left: 638px; }
  .button-divider { position: absolute; left: 598px; top: 526px; width: 1px; height: 31px; background: #9a9a9a; }

  .footer-note {
    position: absolute; left: 302px; top: 596px; font-family: "Nothing You Could Do", cursive;
    font-size: 14px; color: var(--accent-orange); transform: rotate(-3deg); white-space: nowrap;
  }
  .footer-nav { position: absolute; left: 110px; top: 623px; font-size: 14.5px; color: var(--text-dark); white-space: nowrap; }
  .footer-nav .current { color: var(--brand-blue); }
  .footer-nav .struck { text-decoration: line-through; text-decoration-color: var(--strike-red); text-decoration-thickness: 2px; }
  .footer-nav .sep { margin: 0 5px; }

  .follow { position: absolute; left: 911px; top: 622px; display: flex; align-items: center; gap: 9px; font-size: 14.5px; color: var(--text-dark); }
  .follow-label { margin-right: 4px; }
  .social-square { width: 22px; height: 22px; border-radius: 3px; }
  .social-one { background: #5fb7e4; }
  .social-two { background: #3b5a98; }
  .social-three { background: #4a4a4a; }
</style>
</head>
<body>
<div class="canvas">
  <header>
    <div class="brand">
      <span class="brand-dot"></span>
      <span class="brand-name">Pondly.io</span>
    </div>
    <a class="access-link">Access your shares</a>
  </header>

  <main class="hero-panel"></main>

  <div class="arrow-area arrow-left" role="img" aria-label="Curved hand-drawn arrow pointing to the headline"></div>
  <div class="arrow-area arrow-right" role="img" aria-label="Hand-drawn arrow pointing to the headline"></div>

  <p class="script script-fast">Certified fastest<br>sharing in the market</p>
  <p class="script script-social">It's social!</p>

  <h1 class="headline">Share NOW</h1>

  <p class="tagline">Drag information, add people</p>
  <div class="boom" role="img" aria-label="Orange starburst badge">BOOM!</div>

  <nav class="categories">
    Files<span class="sep">|</span>Pictures<span class="sep">|</span>Tasks<span class="sep">|</span>To-dos<span class="sep">|</span>Calendars<span class="sep">|</span>Notes<span class="sep">|</span>Links
  </nav>

  <div class="drop-zone">
    <svg class="drop-plus" viewBox="0 0 48 48" aria-hidden="true">
      <rect x="18" y="0" width="12" height="48" fill="#5b98cd"/>
      <rect x="0" y="18" width="48" height="12" fill="#5b98cd"/>
    </svg>
    <p class="drop-text">Drag Files here<br>to Share Immediately</p>
  </div>

  <span class="or-word">Or</span>

  <div class="email-field">Enter Business Email</div>
  <div class="start-button">Start Sharing</div>

  <div class="info-button button-what">
    <svg viewBox="0 0 26 26" aria-hidden="true">
      <circle cx="13" cy="13" r="11.5" fill="none" stroke="#ffffff" stroke-width="2"/>
      <path d="M9.5,10 Q9.5,6.5 13,6.5 Q16.5,6.5 16.5,9.8 Q16.5,12 13.5,13.2 L13,15.5" fill="none" stroke="#ffffff" stroke-width="2.2" stroke-linecap="round"/>
      <circle cx="13" cy="19.2" r="1.5" fill="#ffffff"/>
    </svg>
    What is it ?
  </div>
  <span class="button-divider"></span>
  <div class="info-button button-video">
    <svg viewBox="0 0 26 26" aria-hidden="true">
      <rect x="2" y="9" width="22" height="15" rx="1.5" fill="#1f2a36"/>
      <polygon points="2,4 23,1 24,6 3,9" fill="#1f2a36"/>
      <polygon points="10,13 18,16.5 10,20" fill="#6ab0e6"/>
    </svg>
    Watch Video
  </div>

  <footer>
    <span class="footer-note">Free for unlimited users</span>
    <nav class="footer-nav">
      <span class="current">Home</span><span class="sep">|</span>About us<span class="sep">|</span>Product Tour<span class="sep">|</span><span class="struck">Pricing</span><span class="sep">|</span>Terms of use<span class="sep">|</span>Jobs<span class="sep">|</span>Sign up<span class="sep">|</span>Blog<span class="sep">|</span>Press<span class="sep">|</span>Contact us
    </nav>
    <div class="follow">
      <span class="follow-label">Follow us :</span>
      <span class="social-square social-one" role="img" aria-label="Social network link"></span>
      <span class="social-square social-two" role="img" aria-label="Social network link"></span>
      <span class="social-square social-three" role="img" aria-label="Social network link"></span>
    </div>
  </footer>
</div>
</body>
</html>
```